Designer and consultant for professionals/businesses and manufacturers in the kitchen and bath in...

I have 30 years of design experience, and 19 of those years within the marketing team of a national cabinet manufacturer. This role gave me the opportunity to consult and design for kitchen/bath businesses, from boutique to multi-store national scale. My services include layout and spatial planning, individual display design, and product design for cabinet manufacturers. From showrooms, to trade shows to integrated design collections. I would like to see designs that convey professionalism, as well as an appeal to the creative designer mind!

Target Market(s)

Kitchen and bath dealers, as well as mid-scale multi-store home centers. Cabinet manufacturers, Trade Show agencies.

Industry/Entity Type

Kitchen

Contact Information for Business Card

Serving Kitchen and Bath Businesses

Logo Text

MT (initials for business name)

Font styles to use
Serif
Sans Serif
Decorative

Colors
e34197

Requirements
Must have
• Marla Tovey Design and Consulting, Inc. (business name)
• marla@mtvexor.com (email)
• 917-555-0148 (phone)
• mtvexor.com (website)
Nice to have
• Inclusions of geometric shapes; particularly a 30/15 degree triangle and circle(s)
• 2 colors
Should not have
• Not too artsy!

```html
<!DOCTYPE html>
<html lang="en">
<head>
<meta charset="utf-8">
<title>Marla Tovey Design and Consulting, Inc. – Business Card</title>
<link rel="stylesheet" href="https://fonts.googleapis.com/css2?family=Bodoni+Moda:wght@400&family=Playfair+Display:wght@900&display=swap">
<style>
  :root {
    --steel-blue: #4370a0;
    --frame-grey: #c9cbca;
    --cream: #fcfaeb;
    --ink: #352b2b;
    --accent-pink: #e34197;
  }
  html, body {
    margin: 0;
    padding: 0;
    overflow: hidden;
    background: var(--steel-blue);
  }
  .card {
    position: relative;
    width: 1200px;
    height: 707px;
    overflow: hidden;
    background: var(--steel-blue);
  }
  .card__backdrop {
    position: absolute;
    inset: 0;
  }
  .card__panel {
    position: absolute;
    left: 71px;
    top: 83px;
    width: 691px;
    height: 624px;
    background: var(--steel-blue);
  }
  .company-name {
    position: absolute;
    left: 113px;
    top: 221px;
    margin: 0;
    font-family: "Playfair Display", serif;
    font-weight: 900;
    font-size: 26.5px;
    letter-spacing: 0.1px;
    color: var(--ink);
    white-space: nowrap;
  }
  .contact {
    position: absolute;
    left: 145px;
    margin: 0;
    font-family: "Bodoni Moda", serif;
    font-weight: 400;
    font-size: 33px;
    color: var(--ink);
    white-space: nowrap;
    line-height: 1;
  }
  .contact--email { top: 352px; }
  .contact--phone { top: 437px; }
  .contact--web   { top: 523px; }
  .brand-mark {
    position: absolute;
    left: 805px;
    top: 31px;
    width: 330px;
    height: 330px;
    display: flex;
    align-items: center;
    justify-content: center;
    font-family: "Playfair Display", serif;
    font-weight: 900;
    font-size: 130px;
    color: var(--accent-pink);
    line-height: 1;
  }
</style>
</head>
<body>
  <div class="card">
    <svg class="card__backdrop" width="1200" height="707" viewBox="0 0 1200 707" aria-hidden="true">
      <rect width="1200" height="707" fill="var(--steel-blue)"/>
      <path class="frame" d="M0 56 H848 V328 H841 V707 H0 Z" fill="var(--frame-grey)"/>
      <circle class="badge-ring" cx="970" cy="196" r="181" fill="var(--steel-blue)"/>
      <circle class="badge" cx="970" cy="196" r="165" fill="var(--cream)"/>
    </svg>
    <div class="card__panel"></div>

    <div class="brand-mark">MT</div>

    <h1 class="company-name">Marla Tovey Design and Consulting, Inc.</h1>
    <p class="contact contact--email">marla@mtvexor.com</p>
    <p class="contact contact--phone">917-555-0148</p>
    <p class="contact contact--web">mtvexor.com</p>
  </div>
</body>
</html>
```